Customer Upgrade from Free to Paid Investment Management

Our intent is to have customers that use our free online service consider converting into our paid investment management service.

In current vernacular, we have a Freemium business proposition - but we are just at the early stages of building out our upgrade capabilities.

The design request is detailed in the attached file, but essentially, I'm looking to add another banner to our library. Let me see what you can do!

Target Market(s)

40s-50s, can have any balance in their 401k, at first thought they could manage their 401k themselves, but may be interested in having us manage.

Industry/Entity Type

Investment

Requirements
Must have
• Keep it very simple.
Banner specs are attached in the file
Should not have
• No animation
No "hard sell"

```html
<!DOCTYPE html>
<html lang="en">
<head>
<meta charset="UTF-8">
<title>Upgrade Banner – Personalized Plan</title>
<link rel="stylesheet" href="https://fonts.googleapis.com/css2?family=Arimo:wght@400;700&display=swap">
<style>
  :root {
    --page-bg: #ffffff;
    --banner-top: #f6fafc;
    --banner-bottom: #dcedf4;
    --banner-border: #cfe1ea;
    --headline: #f47b20;
    --subline: #4a4a4a;
    --target-light: #f2f2f2;
    --target-mid: #c6c6c6;
    --btn-top: #9fcf63;
    --btn-bottom: #6ea636;
    --btn-edge: #5a8e2a;
    --btn-text: #ffffff;
  }
  * { margin: 0; padding: 0; box-sizing: border-box; }
  html, body {
    width: 1200px;
    height: 900px;
    overflow: hidden;
    background: var(--page-bg);
    font-family: "Arimo", Arial, sans-serif;
  }
  .canvas {
    position: relative;
    width: 1200px;
    height: 900px;
  }
  .upgrade-banner {
    position: absolute;
    left: 83px;
    top: 405px;
    width: 1035px;
    height: 119px;
    border: 1.5px solid var(--banner-border);
    border-radius: 9px;
    background: linear-gradient(to bottom, var(--banner-top), var(--banner-bottom));
  }
  .target-art {
    position: absolute;
    left: 102px;
    top: 375px;
    width: 130px;
    height: 150px;
    border-radius: 50%;
    background: radial-gradient(circle at 45% 50%, var(--target-light) 0%, var(--target-mid) 55%, var(--target-light) 100%);
  }
  .banner-copy {
    position: absolute;
    left: 282px;
    top: 431px;
  }
  .headline {
    font-size: 30px;
    font-weight: 700;
    color: var(--headline);
    line-height: 36px;
    letter-spacing: -0.2px;
  }
  .subline {
    font-size: 19.5px;
    font-weight: 400;
    color: var(--subline);
    line-height: 26px;
    margin-top: 1px;
  }
  .learn-more {
    position: absolute;
    left: 930px;
    top: 444px;
    width: 172px;
    height: 42px;
    display: block;
    text-decoration: none;
  }
  .learn-more svg {
    position: absolute;
    inset: 0;
  }
  .learn-more span {
    position: absolute;
    left: 19px;
    top: 0;
    line-height: 40px;
    font-size: 21px;
    font-weight: 700;
    color: var(--btn-text);
    text-shadow: 0 1px 2px rgba(40, 70, 15, 0.7);
    letter-spacing: -0.2px;
  }
</style>
</head>
<body>
  <main class="canvas">
    <section class="upgrade-banner" aria-label="Personalized plan offer"></section>
    <div class="target-art" role="img" aria-label="Illustration of a dartboard target with a dart in the bullseye"></div>
    <div class="banner-copy">
      <h1 class="headline">Not sure what to do from here?</h1>
      <p class="subline">A complete plan personalized for you.</p>
    </div>
    <a class="learn-more" href="#">
      <svg width="172" height="42" viewBox="0 0 172 42" aria-hidden="true">
        <defs>
          <linearGradient id="btn-fill" x1="0" y1="0" x2="0" y2="1">
            <stop offset="0" stop-color="var(--btn-top)"/>
            <stop offset="0.5" stop-color="var(--btn-top)"/>
            <stop offset="0.5" stop-color="var(--btn-bottom)"/>
            <stop offset="1" stop-color="var(--btn-bottom)"/>
          </linearGradient>
        </defs>
        <polygon points="1,1 155,1 170,21 155,41 1,41" fill="url(#btn-fill)" stroke="var(--btn-edge)" stroke-width="1.5" stroke-linejoin="round"/>
      </svg>
      <span>Learn more</span>
    </a>
  </main>
</body>
</html>
```